Corporate Letterhead

Looking for a new corporate letterhead design. Our colors are orange and gray.

We'd like it if the below could be included somehow in the letterhead.                                       

Partnerships | Results | Quality

• Logo, Company Name, Address, Phone #, Fax #, Web address, Email address (optional), the phrase "A Service Disable Veteran Owned Small Business".

```html
<!DOCTYPE html>
<html lang="en">
<head>
<meta charset="utf-8">
<title>Veridian Systems, Inc — Letterhead</title>
<link rel="stylesheet" href="https://fonts.googleapis.com/css2?family=Source+Sans+3:wght@400;600&family=Arimo:wght@400;700&display=swap">
<style>
  :root {
    --orange: #f39022;
    --orange-soft: #fdeedb;
    --gray: #7a7a7a;
    --gray-dark: #333333;
    --rule: #bdbdbd;
    --paper: #ffffff;
  }
  * { box-sizing: border-box; margin: 0; padding: 0; }
  html, body { width: 875px; height: 1200px; overflow: hidden; background: var(--paper); }
  .letterhead {
    position: relative;
    width: 875px;
    height: 1200px;
    background: var(--paper);
    font-family: "Source Sans 3", sans-serif;
    color: var(--gray-dark);
    overflow: hidden;
  }
  .brand {
    position: absolute;
    left: 33px;
    top: 34px;
    display: flex;
    align-items: center;
    gap: 16px;
  }
  .brand-dot {
    width: 56px;
    height: 56px;
    border-radius: 50%;
    background: var(--orange);
  }
  .brand-name {
    font-family: "Arimo", sans-serif;
    font-weight: 700;
    font-size: 30px;
    letter-spacing: 0.5px;
    color: var(--orange);
    text-transform: uppercase;
  }
  .address {
    position: absolute;
    left: 631px;
    top: 41px;
    height: 48px;
    padding-left: 12px;
    border-left: 1px solid var(--rule);
    font-size: 14px;
    line-height: 20px;
    padding-top: 4px;
  }
  .corner-wash {
    position: absolute;
    right: 0;
    bottom: 0;
    width: 420px;
    height: 300px;
    background: radial-gradient(ellipse at 100% 100%, var(--orange-soft) 0%, rgba(253,238,219,0.5) 45%, rgba(255,255,255,0) 75%);
  }
  .contacts {
    position: absolute;
    left: 23px;
    top: 1085px;
    list-style: none;
    font-size: 14px;
    line-height: 20.5px;
  }
  .contacts li { display: flex; align-items: center; gap: 7px; }
  .contacts svg { width: 13px; height: 13px; flex: none; }
  .designation {
    position: absolute;
    left: 23px;
    top: 1173px;
    font-family: "Arimo", sans-serif;
    font-size: 14.5px;
    letter-spacing: 1px;
    color: var(--orange);
  }
  .values {
    position: absolute;
    left: 700px;
    top: 1094px;
    width: 124px;
    text-align: center;
    font-family: "Arimo", sans-serif;
    font-size: 17px;
    line-height: 24.5px;
    color: var(--gray);
    list-style: none;
  }
  .values .accent { color: var(--orange); }
</style>
</head>
<body>
<main class="letterhead">
  <header>
    <div class="brand">
      <span class="brand-dot"></span>
      <span class="brand-name">Veridian Systems, Inc</span>
    </div>
    <address class="address" style="font-style:normal">
      4210 Commerce Drive<br>
      Suite 210, Linthicum, MD 21090
    </address>
  </header>

  <div class="corner-wash"></div>

  <footer>
    <ul class="contacts">
      <li>
        <svg viewBox="0 0 14 14" aria-hidden="true"><circle cx="7" cy="7" r="6.3" fill="none" stroke="#f39022" stroke-width="1.2"/><path d="M5 3.6c-.8.5-1 1.6-.4 3 .6 1.5 1.8 2.9 3 3.5.7.3 1.3.2 1.7-.3l-1.1-1.2-.7.4c-.6-.3-1.3-1.2-1.6-1.9l.5-.6L5 3.6z" fill="#f39022"/></svg>
        443-555-0142
      </li>
      <li>
        <svg viewBox="0 0 14 14" aria-hidden="true"><rect x="4" y="1" width="6" height="4" fill="#f39022"/><rect x="1" y="5" width="12" height="6" rx="1" fill="#f39022"/><rect x="4" y="9" width="6" height="4" fill="#ffffff" stroke="#f39022" stroke-width="1"/></svg>
        410-555-0187
      </li>
      <li>
        <svg viewBox="0 0 14 14" aria-hidden="true"><rect x="1" y="3" width="12" height="9" rx="1.5" fill="#f39022"/><path d="M2 4.5l5 3.5 5-3.5" fill="none" stroke="#fff" stroke-width="1.2"/></svg>
        info@veridiansysinc.com
      </li>
      <li>
        <svg viewBox="0 0 14 14" aria-hidden="true"><circle cx="7" cy="7" r="6" fill="#f39022"/><ellipse cx="7" cy="7" rx="2.5" ry="6" fill="none" stroke="#fff" stroke-width="0.9"/><path d="M1 7h12M2 4h10M2 10h10" stroke="#fff" stroke-width="0.9"/></svg>
        www.veridiansysinc.com
      </li>
    </ul>
    <p class="designation">A Service Disable Veteran Owned Small Business</p>
    <ul class="values">
      <li>Partnerships</li>
      <li class="accent">Results</li>
      <li>Quality</li>
    </ul>
  </footer>
</main>
</body>
</html>
```